Financial Advisor Resource Firm needs business card design

Need business card design for company in Omaha NE called Tallowbrook Partners. We provide resources to financial advisors....workshop programs, retirement analysis, and insurance planning. I would like to see designs that use grays, greens, black, and white colors. The final design should communicate 'collaboration' and be simple yet attractive to financial planning clients. I will attached our logo and another picture of a puzzle piece coming together. I would like the incorporate the puzzle picture somehow, maybe on the back somehow, with color or just the gray scale....OR, the picture be the front of the card with 'Tallowbrook' definition on it (see upload) and then company logo, employee name, title, address on the back (see ppt uploaded). The following disclosure needs to be included somewhere- Advisory services offered through Marlowe Ridge Advisors, LLC.
Updates

I uploaded a svg and ai file of the logo

Target Market(s)

Financial planning clients and financial advisors....so pretty diverse age range of about 40-70.

Industry/Entity Type

Financial Planning

Contact Information for Business Card

Dennis K. Holloway, MBA
Founder/President
5727 E. Larkspur Avenue
Suite 418
Omaha, NE 68297
Phone- (402) 555-0147
Cell- (402) 555-0183
Fax- (402) 555-0129
email- dennis@tallowbrookgroup.example
web address- www.tallowbrookgroup.example

Colors
1b1b1b
474747
d3d3d3
ffffff
9bcb3c
abd036

Requirements
Must have
• Must include logo provided, must be 2 sided, and must have disclosure...all of these items listed in project description

```html
<!DOCTYPE html>
<html lang="en">
<head>
<meta charset="utf-8">
<title>Tallowbrook Partners – Business Card</title>
<link href="https://fonts.googleapis.com/css2?family=Roboto:wght@400;500;700&display=swap" rel="stylesheet">
<style>
  :root {
    --ink: #1b1b1b;
    --slate: #474747;
    --mist: #d3d3d3;
    --paper: #ffffff;
    --leaf: #9bcb3c;
    --lime: #abd036;
    --leaf-deep: #4f8f2a;
    --backdrop: #e9ebe6;
  }
  * { margin: 0; padding: 0; box-sizing: border-box; }
  html, body {
    width: 1200px; height: 900px; overflow: hidden;
    background: var(--backdrop);
    font-family: "Roboto", Arial, sans-serif;
  }
  .canvas {
    position: relative; width: 1200px; height: 900px;
  }
  .card {
    position: absolute; left: 250px; width: 700px; height: 400px;
    box-shadow: 0 6px 18px rgba(27,27,27,0.18);
    overflow: hidden;
  }
  .card--front { top: 40px; background: var(--paper); }
  .card--back { top: 470px; }

  /* wordmark */
  .wordmark {
    position: absolute; display: flex; align-items: center; gap: 12px;
  }
  .wordmark__dot {
    width: 18px; height: 18px; border-radius: 50%; background: var(--leaf);
  }
  .wordmark__name {
    font-size: 30px; font-weight: 500; letter-spacing: 1px;
    text-transform: uppercase;
  }
  .card--front .wordmark { left: 44px; top: 48px; }
  .card--front .wordmark__name { color: var(--slate); }

  /* contact block */
  .contact {
    position: absolute; left: 44px; top: 150px;
    color: var(--slate); font-size: 15px; line-height: 1.5;
  }
  .contact__rule {
    width: 28px; height: 3px; background: var(--leaf); margin: 12px 0;
  }
  .contact__label { color: var(--leaf); margin-right: 4px; }

  .person {
    position: absolute; right: 44px; top: 178px; text-align: right;
  }
  .person__name {
    color: var(--leaf); font-size: 22px; font-weight: 700;
  }
  .person__title {
    color: var(--slate); font-size: 16px; margin-top: 4px;
  }

  /* back */
  .back__photo {
    position: absolute; inset: 0;
    background:
      radial-gradient(ellipse at 35% 45%, rgba(171,208,54,0.55), transparent 60%),
      linear-gradient(135deg, #7fb83a 0%, var(--leaf) 45%, #5e9e2e 100%);
  }
  .card--back .wordmark { left: 60px; top: 150px; }
  .card--back .wordmark__dot { background: var(--paper); }
  .card--back .wordmark__name { color: var(--paper); font-size: 38px; }
  .disclosure {
    position: absolute; left: 60px; right: 44px; bottom: 40px;
    display: flex; align-items: center; gap: 18px;
    color: var(--paper); font-size: 14px; line-height: 1.4;
  }
  .disclosure__line { flex: 1; height: 1px; background: rgba(255,255,255,0.8); }
  .disclosure__text { text-align: right; }
</style>
</head>
<body>
<main class="canvas">

  <section class="card card--front" aria-label="Card front">
    <div class="wordmark">
      <span class="wordmark__dot"></span>
      <span class="wordmark__name">Tallowbrook Partners</span>
    </div>

    <address class="contact" style="font-style:normal">
      <div>5727 E. Larkspur Avenue</div>
      <div>Suite 418, Omaha, NE 68297</div>
      <div class="contact__rule"></div>
      <div><span class="contact__label">P.</span>(402) 555-0147</div>
      <div><span class="contact__label">M.</span>(402) 555-0183</div>
      <div><span class="contact__label">F.</span>(402) 555-0129</div>
      <div>dennis@tallowbrookgroup.example</div>
      <div>www.tallowbrookgroup.example</div>
    </address>

    <div class="person">
      <div class="person__name">Dennis K. Holloway, MBA</div>
      <div class="person__title">Founder/President</div>
    </div>
  </section>

  <section class="card card--back" aria-label="Card back">
    <div class="back__photo" role="img" aria-label="Green-toned photo of hands fitting puzzle pieces together"></div>
    <div class="wordmark">
      <span class="wordmark__dot"></span>
      <span class="wordmark__name">Tallowbrook Partners</span>
    </div>
    <div class="disclosure">
      <span class="disclosure__line"></span>
      <span class="disclosure__text">Advisory services offered through<br>Marlowe Ridge Advisors, LLC</span>
    </div>
  </section>

</main>
</body>
</html>
```